Business Card Design

Hoping for a black background business card, minimalistic design.
With the Marble Crest logo you created in white.

I would like to include:
My Name and title
Address (street address)
Reception: (phone number)
Fax: (fax number)
Reception: (email address)
Direct email: (email address)
Instagram: (ig handle)

```html
<!DOCTYPE html>
<html lang="en">
<head>
<meta charset="utf-8">
<title>Marble Crest – Business Card</title>
<link rel="stylesheet" href="https://fonts.googleapis.com/css2?family=Montserrat:wght@300;400;500&display=swap">
<style>
  :root {
    --page-bg: #e4e5e6;
    --card-bg: #070809;
    --ink: #ffffff;
    --ink-soft: #d9d9d9;
    --ring-faint: #1e1f21;
  }
  * { box-sizing: border-box; margin: 0; padding: 0; }
  html, body {
    width: 1200px; height: 1200px; overflow: hidden;
    background: var(--page-bg);
    font-family: "Montserrat", sans-serif;
  }
  .card {
    position: absolute; left: 158px; width: 882px; height: 520px;
    background: var(--card-bg); overflow: hidden;
  }
  .card--front { top: 56px; }
  .card--back { top: 609px; }

  .deco-ring { position: absolute; left: 0; top: 0; }

  .brand { position: absolute; display: flex; align-items: center; color: var(--ink); }
  .brand__dot { border: solid var(--ink); border-radius: 50%; flex: none; }
  .brand__name { font-weight: 400; text-transform: uppercase; white-space: nowrap; line-height: 1; }

  .card--front .brand { left: 34px; top: 57px; gap: 24px; }
  .card--front .brand__dot { width: 100px; height: 100px; border-width: 5px; }
  .card--front .brand__name { font-size: 30px; letter-spacing: 1.5px; }

  .card--back .brand { left: 117px; top: 181px; gap: 42px; }
  .card--back .brand__dot { width: 150px; height: 150px; border-width: 7px; }
  .card--back .brand__name { font-size: 50px; letter-spacing: 2.5px; }

  .holder {
    position: absolute; left: 60px; top: 228px;
    color: var(--ink); font-weight: 500; font-size: 26px;
    letter-spacing: 0.8px; text-transform: uppercase; line-height: 1.2;
  }

  .contact { list-style: none; position: absolute; left: 60px; top: 0; }
  .contact__item {
    position: absolute; left: 0; display: flex; align-items: center; gap: 16px;
    color: var(--ink-soft); font-weight: 300; font-size: 20px; white-space: nowrap;
    transform: translateY(-50%);
  }
  .contact__icon { width: 18px; height: 18px; fill: var(--ink-soft); flex: none; }

  .social {
    position: absolute; right: 54px; top: 459px; transform: translateY(-50%);
    display: flex; align-items: center; gap: 9px;
    color: var(--ink-soft); font-weight: 300; font-size: 20px;
  }
  .social__dot { width: 15px; height: 15px; border: 2px solid var(--ink-soft); border-radius: 50%; }
</style>
</head>
<body>

<section class="card card--front" aria-label="Business card front">
  <svg class="deco-ring" width="882" height="520" aria-hidden="true">
    <circle cx="754" cy="175" r="131" fill="none" stroke="var(--ring-faint)" stroke-width="6"/>
  </svg>

  <div class="brand">
    <span class="brand__dot"></span>
    <span class="brand__name">Marble Crest</span>
  </div>

  <h1 class="holder">Daniel Hargreave</h1>

  <ul class="contact">
    <li class="contact__item" style="top:314px">
      <svg class="contact__icon" viewBox="0 0 24 24" aria-label="Reception phone"><path d="M6.6 10.8a15.1 15.1 0 0 0 6.6 6.6l2.2-2.2a1 1 0 0 1 1-.25 11.4 11.4 0 0 0 3.6.57 1 1 0 0 1 1 1V20a1 1 0 0 1-1 1A17 17 0 0 1 3 4a1 1 0 0 1 1-1h3.5a1 1 0 0 1 1 1c0 1.25.2 2.45.57 3.57a1 1 0 0 1-.25 1z"/></svg>
      <span>0400 318 725</span>
    </li>
    <li class="contact__item" style="top:348px">
      <svg class="contact__icon" viewBox="0 0 24 24" aria-label="Fax"><path d="M6 2h12v5H6zM3 8h18a1 1 0 0 1 1 1v8h-4v5H6v-5H2V9a1 1 0 0 1 1-1zm5 7v5h8v-5zm1 1h6v1H9zm0 2h6v1H9z"/></svg>
      <span>07 5494 2210</span>
    </li>
    <li class="contact__item" style="top:382px">
      <svg class="contact__icon" viewBox="0 0 24 24" aria-label="Reception email"><path d="M2 5h20v14H2zm2 2v.4l8 5.6 8-5.6V7zm0 2.8V17h16V9.8l-8 5.6z"/></svg>
      <span>info@marblecrest.com.au</span>
    </li>
    <li class="contact__item" style="top:415px">
      <svg class="contact__icon" viewBox="0 0 24 24" aria-label="Direct email"><path d="M2 5h20v14H2zm2 2v.4l8 5.6 8-5.6V7zm0 2.8V17h16V9.8l-8 5.6z"/></svg>
      <span>daniel@marblecrest.com.au</span>
    </li>
    <li class="contact__item" style="top:459px">
      <svg class="contact__icon" viewBox="0 0 24 24" aria-label="Address"><path d="M12 1a6 6 0 0 0-6 6c0 4.5 6 11 6 11s6-6.5 6-11a6 6 0 0 0-6-6zm0 8.3A2.3 2.3 0 1 1 12 4.7a2.3 2.3 0 0 1 0 4.6zM4 19h16v3H4z"/></svg>
      <span>42 Linden Way Maleny Q 4552</span>
    </li>
  </ul>

  <div class="social">
    <span class="social__dot"></span>
    <span>marblecrest</span>
  </div>
</section>

<section class="card card--back" aria-label="Business card back">
  <div class="brand">
    <span class="brand__dot"></span>
    <span class="brand__name">Marble Crest</span>
  </div>
</section>

</body>
</html>
```